Meridel Voyages Website Redesign

Read the Company mission statement and then help us redesign the website along the guidelines in the design brief and using the logo and fonts supplied.

The current meridel voyages website is very dated but has been very sucessful, we would like to invest in a brand refresh and site rebuild to bring the website up to 2018 standard.

We have using cut and paste from other travel websites made a pdf mock up of what sort of content we need on the pages and the lay out we like.

Target Market(s)

+45 Plus experienced meridel voyages, established, educated

Number of Pages Required

4 page

Font styles to use
Sans Serif

Requirements
Must have
• There is a full brief document and mock up, it must follow the brand guidelines
Nice to have
• There is a full brief document and mock up
Should not have
• Looks of a cheap cruise deal travel site

```html
<!DOCTYPE html>
<html lang="en">
<head>
<meta charset="utf-8">
<title>Meridel Voyages</title>
<link rel="stylesheet" href="https://fonts.googleapis.com/css2?family=Noto+Sans:wght@400;600;700&display=swap">
<style>
:root{
  --navy:#0d2d63;
  --blue:#1a73c7;
  --button:#1f8be6;
  --text:#2e2e2e;
  --muted:#555;
  --card:#f4f3f1;
  --gold:#eaa60d;
  --white:#fff;
}
*{box-sizing:border-box;margin:0;padding:0}
html,body{width:1200px;height:1198px;overflow:hidden;background:var(--white);font-family:"Noto Sans",sans-serif;color:var(--text)}
.page{position:relative;width:1200px;height:1198px;overflow:hidden}
.accent{position:absolute;inset:0;z-index:0}
.site-header{position:absolute;top:0;left:0;width:1200px;height:80px;background:var(--white);z-index:2}
.brand{position:absolute;left:144px;top:26px;display:flex;align-items:center;gap:8px;font-size:20px;font-weight:600;color:var(--blue)}
.brand-dot{width:14px;height:14px;border-radius:50%;background:var(--blue)}
.main-nav{position:absolute;top:31px;right:144px;display:flex;gap:23px;font-size:13.5px;font-weight:600}
.main-nav a{text-decoration:none;color:#333}
.main-nav a.active{color:var(--blue)}
.hero{position:absolute;top:80px;left:0;width:1200px;height:434px;z-index:1;
  background:linear-gradient(180deg,#2b5e9e 0%,#4a86c0 42%,#3f93a8 62%,#58b0b4 80%,#7bbfb8 100%)}
.hero-title{position:absolute;top:125px;width:100%;text-align:center;color:var(--white);font-size:41px;font-weight:700;letter-spacing:.5px;text-shadow:0 2px 4px rgba(0,0,0,.3)}
.hero-text{position:absolute;top:190px;left:260px;width:680px;text-align:center;color:var(--white);font-size:21px;line-height:28px;text-shadow:0 1px 3px rgba(0,0,0,.35)}
.hero-arrow{position:absolute;top:172px}
.filter-panel{position:absolute;top:514px;left:145px;width:912px;height:183px;z-index:1;
  background:linear-gradient(90deg,#b8cbe3 0%,#c3d1de 50%,#d1dfcf 100%)}
.search-box{position:absolute;top:450px;left:278px;width:644px;height:118px;background:var(--navy);z-index:3}
.search-box h2{margin-top:18px;text-align:center;color:var(--white);font-size:22px;font-weight:700;letter-spacing:.3px}
.search-field{position:absolute;left:31px;top:58px;width:459px;height:38px;background:var(--white);font-size:12px;color:#444;line-height:38px;padding-left:19px}
.search-btn{position:absolute;left:490px;top:58px;width:122px;height:38px;background:var(--button);display:flex;align-items:center;justify-content:center}
.select{position:absolute;width:147px;height:28px;background:var(--white);font-size:11.5px;color:#444;line-height:28px;padding-left:17px;z-index:3;box-shadow:0 1px 2px rgba(0,0,0,.08)}
.select::after{content:"";position:absolute;right:11px;top:11px;border-left:5px solid transparent;border-right:5px solid transparent;border-top:6px solid #777}
.section-title{position:absolute;top:758px;width:100%;text-align:center;font-size:35px;font-weight:700;letter-spacing:1px;color:#2e2e2e;z-index:2}
.journey{position:absolute;top:834px;width:288px;height:331px;background:var(--card);border:1px solid #e6e4e0;z-index:2}
.journey-media{height:198px}
.journey-name{position:absolute;left:24px;top:209px;width:180px;font-size:15px;font-weight:600;line-height:19px;letter-spacing:.3px}
.journey-sub{position:absolute;left:24px;top:254px;font-size:13px;color:var(--muted)}
.journey-from{position:absolute;left:223px;top:211px;font-size:11.5px;color:var(--muted)}
.journey-price{position:absolute;left:222px;top:232px;font-size:13.5px;font-weight:600;color:#444}
.carousel-arrow{position:absolute;top:986px;z-index:2}
</style>
</head>
<body>
<div class="page">
  <svg class="accent" width="1200" height="1198" aria-hidden="true"><polygon points="1200,662 1200,1198 922,1198" fill="var(--gold)"/></svg>

  <header class="site-header">
    <div class="brand"><span class="brand-dot"></span>Meridel Voyages</div>
    <nav class="main-nav">
      <a class="active" href="#">Home</a>
      <a href="#">About Us</a>
      <a href="#">Our Cruises</a>
      <a href="#">Contact</a>
    </nav>
  </header>

  <section class="hero" role="img" aria-label="Cruise ship anchored off a tropical palm-lined beach with a seabird overhead">
    <h1 class="hero-title">WELCOME TO MERIDEL VOYAGES</h1>
    <p class="hero-text">Lorem Ipsum is simply dummy text of the printing and typesetting industry.&nbsp; Lorem Ipsum has been the industry's standard text</p>
    <svg class="hero-arrow" style="left:38px" width="26" height="46" aria-hidden="true"><polyline points="22,2 4,23 22,44" fill="none" stroke="rgba(255,255,255,.7)" stroke-width="3"/></svg>
    <svg class="hero-arrow" style="left:1134px" width="26" height="46" aria-hidden="true"><polyline points="4,2 22,23 4,44" fill="none" stroke="rgba(255,255,255,.7)" stroke-width="3"/></svg>
  </section>

  <div class="filter-panel"></div>

  <div class="search-box">
    <h2>TRAVEL WITH PERSONALITY</h2>
    <div class="search-field">Where do you feel like going?</div>
    <div class="search-btn">
      <svg width="20" height="20" viewBox="0 0 20 20" aria-hidden="true"><circle cx="8" cy="8" r="6" fill="none" stroke="#fff" stroke-width="2.6"/><line x1="12.5" y1="12.5" x2="18" y2="18" stroke="#fff" stroke-width="2.8" stroke-linecap="round"/></svg>
    </div>
  </div>

  <div class="select" style="left:277px;top:592px">Any Destination</div>
  <div class="select" style="left:443px;top:592px">Any Sailing Date</div>
  <div class="select" style="left:609px;top:592px">Any Length</div>
  <div class="select" style="left:775px;top:592px">Any Cruise Line</div>
  <div class="select" style="left:277px;top:630px">Any Cruise Ship</div>
  <div class="select" style="left:443px;top:630px">Any Departure Port</div>
  <div class="select" style="left:609px;top:630px">Any Price Range</div>
  <div class="select" style="left:775px;top:630px">Search Cruises</div>

  <h2 class="section-title">FEATURED JOURNEYS</h2>

  <svg class="carousel-arrow" style="left:104px" width="16" height="26" aria-hidden="true"><polyline points="13,2 3,13 13,24" fill="none" stroke="#666" stroke-width="2.4"/></svg>
  <svg class="carousel-arrow" style="left:1082px" width="16" height="26" aria-hidden="true"><polyline points="3,2 13,13 3,24" fill="none" stroke="#444" stroke-width="2.4"/></svg>

  <article class="journey" style="left:145px">
    <div class="journey-media" role="img" aria-label="Aerial view of a sailing ship on a river through dense rainforest" style="background:linear-gradient(160deg,#3f8a3a 0%,#2a6f8f 45%,#357a30 70%,#5a9a3e 100%)"></div>
    <h3 class="journey-name">Lorem Ipsum is simply dummy text</h3>
    <span class="journey-from">From</span><span class="journey-price">$2,470</span>
    <p class="journey-sub">Lorem Ipsum</p>
  </article>

  <article class="journey" style="left:457px">
    <div class="journey-media" role="img" aria-label="Expedition boat among ice floes with walruses in the foreground" style="background:linear-gradient(180deg,#4a8fd0 0%,#a9cfe6 35%,#4cb7c8 60%,#d8eef2 78%,#7a5a45 100%)"></div>
    <h3 class="journey-name">Lorem Ipsum is simply dummy text</h3>
    <span class="journey-from">From</span><span class="journey-price">$2,470</span>
    <p class="journey-sub">Lorem Ipsum</p>
  </article>

  <article class="journey" style="left:769px">
    <div class="journey-media" role="img" aria-label="Cruise ship beside a tropical beach with palms and a seabird" style="background:linear-gradient(180deg,#2b5e9e 0%,#4a86c0 45%,#3f93a8 65%,#7bbfb8 100%)"></div>
    <h3 class="journey-name">Lorem Ipsum is simply dummy text</h3>
    <span class="journey-from">From</span><span class="journey-price">$2,470</span>
    <p class="journey-sub">Lorem Ipsum</p>
  </article>
</div>
</body>
</html>
```